Visually Compelling Flyer Design - Harbor Perks

We are a life insurance company looking to create visually compelling flyers that gain attention of potential buyers and simplify the concept. It should be professional, friendly, approachable in nature. Our logo and several rough drafts are included.
We are looking to refine this look and make it ultra professional, clean and easy to follow. A creative brief with brand guidelines is also included.
FLYER 1 — PAY YOURSELF FIRST
EYEBROW TAG
YOUR COMPANY JUST UPGRADED YOUR BENEFITS
HEADLINE
One small decision. A lifetime of protection.
SUBHEADLINE
Permanent life insurance + long-term care coverage, starting at $1 a day.
EYEBROW TAG
CHOOSE YOUR DAILY INVESTMENT
STAT — TIER 1
$1 / day → $20,000 Life Insurance
STAT — TIER 2 (HERO — make this one biggest/most prominent)
$2 / day → $40,000 Life Insurance
★ Most Popular
STAT — TIER 3
$3 / day → $60,000 Life Insurance
CAPTION
Rate locked at enrollment. Benefit never decreases.
EYEBROW TAG
THREE BENEFITS. ONE POLICY.
SUBHEADLINE
Your money works three ways.
CALLOUT — BENEFIT 1
01 | Cash Value Growth
BODY
Averages 6% annually over the last 50 years — guaranteed never to fall below 3%. Better than any savings account. And if you ever need it, you can borrow against it. It's your money.
CALLOUT — BENEFIT 2
02 | Tax-Free Death Benefit
BODY
From day one, your family is protected. The full benefit is paid tax-free to the person you choose — no waiting period, no exceptions. That's your legacy, preserved.
CALLOUT — BENEFIT 3
03 | Long-Term Care Coverage
BODY
70% of Americans will need long-term care. This plan pays 75% of your benefit — upfront and tax-free — to cover those costs while you're still alive. Your retirement savings stay intact. Your family stays protected.
EYEBROW TAG
ALREADY HAVE LIFE INSURANCE THROUGH WORK?
SUBHEADLINE
That's term. It ends when you need it most.
BODY
Term life insurance is designed for temporary needs — protecting your paycheck, your mortgage, your kids while they're home. When you retire, the house is paid off and your children are grown. Term ends because the need ends.
BODY
But one need never ends: your final expenses and the cost of long-term care. This permanent plan stays with you after retirement — when term coverage is gone and getting new coverage is expensive or impossible.
COMPARISON — LEFT COLUMN HEADER
✕ TERM LIFE
COMPARISON — LEFT COLUMN ITEMS
Gets more expensive with age
Ends at retirement
No cash value
Temporary protection only
COMPARISON — RIGHT COLUMN HEADER
✓ THIS PLAN
COMPARISON — RIGHT COLUMN ITEMS
Rate locked forever at enrollment
Stays with you after retirement
Builds real cash value
Permanent protection for life
EYEBROW TAG
WHAT MAKES THIS DIFFERENT
SUBHEADLINE
Built for you. Stays with you.
CALLOUT
✓ Guaranteed Issued
No medical exams. No questions asked. You qualify.
CALLOUT
✓ Group Rate
Because you work here, you get pricing individuals can't access on their own.
CALLOUT
✓ Rate Locked Forever
Your premium never increases. Your benefit never decreases.
CALLOUT
✓ Portable
Change jobs. Retire. Your policy comes with you at the same rate.
CALLOUT
✓ Family Coverage
Protect your spouse and children under the same plan.
SUBHEADLINE
Protect retirement. Preserve dignity. Plan ahead.
CTA
Be on the lookout for your personalized coverage details.
CAPTION
Brokered by Harbor Perks · Underwritten by TrueLedger
FLYER 2 — THE LONG-TERM CARE REALITY
EYEBROW TAG
WHAT MOST PEOPLE DON'T KNOW — BUT SHOULD
HEADLINE
Most Americans are unprepared. You don't have to be.
SUBHEADLINE
The long-term care gap is real — and it affects families like yours.
EYEBROW TAG
THE NUMBERS ARE HARD TO IGNORE
STAT
70%
of Americans age 65 and older will need some form of long-term care during their lifetime.
CAPTION
Source: Pryce & Lomax, Review of Elder Welfare and Civic Planning, 2018
STAT
3–4%
of Americans over 50 own a private long-term care insurance policy. The gap between who needs it and who has it is staggering.
CAPTION
Source: Stroud & Bellamy, QVT Wellness Wire, 2023
STAT
$700 Billion+
Estimated annual U.S. long-term care cost — and it's growing every year.
CAPTION
Source: Delacroix Wynn & Pasternak, Civic Ledger Council, 2020
STAT
$470 Billion
The estimated value of unpaid care provided by family members every year. That's the real cost — measured in time, stress, and financial sacrifice.
CAPTION
Source: Tillman & Osei, Meridian Bureau
STAT
80%
of total long-term care spending goes directly to assist retirees. This isn't a young person's problem. But the time to plan is now.
CAPTION
SUBHEADLINE
Long-term care doesn't just cost money. It costs families.
BODY
When there's no plan in place, the people you love absorb the impact — financially, emotionally, and physically. Retirement savings built over a lifetime can disappear in months. Family members step back from their own lives to provide care. Dignity becomes a daily negotiation.
BODY
This is not inevitable. A small decision today changes the entire outcome.
EYEBROW TAG
THE SOLUTION
HEADLINE
The Pay Yourself First Principle.
BODY
Take the first $1, $2, or $3 you make every day and invest it in a permanent life insurance policy that includes long-term care coverage — underwritten by TrueLedger, offered through your employer at a group rate, and Guaranteed Issued for everyone.
STAT
$1 / day → $20,000 $2 / day → $40,000 $3 / day → $60,000
BODY
The benefit includes three protections in one: a cash value that grows at an average of 6% annually, a tax-free death benefit for your family, and long-term care coverage that pays 75% of your benefit upfront — tax-free — when you need care most.
SUBHEADLINE
Whether you're single, married, with children or without — there is protection in this plan for you.
HEADLINE
CTA
Look for your personalized offer. Coverage details are coming your way.
CAPTION
COPY RULES FOR DESIGNERS
Headlines are one idea only. Never more than two lines.
Stats stand alone. Never buried in a paragraph.
Body copy maxes at 3 sentences per block. If it's longer, cut it.
The $2/day tier is always the hero. Always.
"Guaranteed Issued" appears on both flyers. It's the most important trust signal.
TrueLedger is always attributed. Always.
The tagline is: Protect retirement. Preserve dignity. Plan ahead. — Use it verbatim.
Target Market(s)
Average Americans with a family - adults looking for life insurance
Industry/Entity Type
Life Insurance & Financial Retirement

```html
<!DOCTYPE html>
<html lang="en">
<head>
<meta charset="utf-8">
<title>Harbor Perks — One small decision</title>
<link href="https://fonts.googleapis.com/css2?family=Outfit:wght@300;400;500;600;700;800&display=swap" rel="stylesheet">
<style>
  :root{
    --navy:#232b6b;
    --blue:#1a5cb0;
    --teal:#16a3c2;
    --sky:#5fcbe3;
    --ice:#e3f4fb;
    --mist:#ececec;
    --ink:#3b3f4a;
    --red:#e8425a;
    --green:#2fb59a;
    --backdrop:#0e1626;
  }
  *{box-sizing:border-box;margin:0;padding:0}
  html,body{width:981px;height:1200px;overflow:hidden;background:var(--backdrop);font-family:"Outfit",sans-serif;color:var(--ink)}
  .flyer{position:absolute;left:42px;top:20px;width:896px;height:1160px;background:#fff;overflow:hidden}
  .abs{position:absolute}

  .hero-photo{left:430px;top:0;width:466px;height:460px;
    background:radial-gradient(ellipse at 60% 40%,rgba(255,255,255,0) 0%,rgba(255,255,255,0) 55%,#fff 95%),
    linear-gradient(180deg,#7fb6e0 0%,#b9d8ee 38%,#d9cdb6 62%,#efe6d6 80%,#fff 100%);}
  .hero-photo::after{content:"";position:absolute;inset:0;background:linear-gradient(90deg,#fff 0%,rgba(255,255,255,0) 35%)}

  .brand{left:50px;top:40px;display:flex;align-items:center;gap:12px}
  .brand-dot{width:78px;height:78px;border-radius:50%;background:var(--teal)}
  .brand-name{font-weight:700;font-size:34px;line-height:1;color:var(--blue);letter-spacing:.5px}

  .seal{left:443px;top:38px;width:120px;height:120px;border-radius:50%;background:var(--blue);
    display:flex;flex-direction:column;align-items:center;justify-content:center;color:#fff;font-weight:800;line-height:1.05;text-align:center}
  .seal .top{font-size:15px;letter-spacing:.3px}
  .seal .bottom{font-size:20px}

  .headline{left:54px;top:152px;font-weight:700;font-size:45px;line-height:49px;color:var(--navy);letter-spacing:-.8px}
  .subhead{left:55px;top:258px;font-weight:300;font-size:20px;line-height:24px;color:#2e3340}
  .subhead b{font-weight:700;color:var(--teal)}

  .rule-title{left:58px;width:800px;display:flex;align-items:center;gap:12px}
  .rule-title::before,.rule-title::after{content:"";flex:1;height:1px;background:var(--teal)}
  .rule-title span{font-weight:700;color:var(--navy);white-space:nowrap}
  .choose{top:336px}.choose span{font-size:17px}
  .rate-note{top:568px}.rate-note span{font-size:14.5px;font-weight:400;color:var(--navy);display:flex;align-items:center;gap:6px}

  .tier{top:374px;width:234px;height:176px;border:1.5px solid #dfe3e8;border-radius:22px;background:#fff;
    display:flex;flex-direction:column;align-items:center;padding-top:12px}
  .tier .price{display:flex;align-items:baseline;gap:9px;color:var(--teal)}
  .tier .price strong{font-weight:800;font-size:60px;line-height:62px}
  .tier .price em{font-style:normal;font-weight:500;font-size:16px}
  .tier .arrow{margin:6px 0 8px;width:40px;height:10px}
  .tier .amount{font-weight:700;font-size:33px;line-height:34px;color:var(--navy)}
  .tier .label{font-weight:600;font-size:15.5px;color:var(--navy);margin-top:3px}
  .tier-1{left:71px}.tier-3{left:620px}
  .tier-2{left:345px;width:235px;border:none;background:linear-gradient(135deg,#1c8fd0 0%,#1a5cb0 60%,#1b4a9c 100%);overflow:hidden;padding-right:30px}
  .tier-2 .price,.tier-2 .amount,.tier-2 .label{color:#fff}
  .tier-2 .amount{font-size:33px}
  .tier-2 .label{font-size:16px}
  .popular{position:absolute;right:0;top:0;width:30px;height:100%;background:var(--navy);display:flex;align-items:center;justify-content:center}
  .popular span{transform:rotate(-90deg);white-space:nowrap;color:#fff;font-weight:600;font-size:10.5px;letter-spacing:.8px}
  .tab{top:415px;width:29px;height:76px;border-radius:15px;display:flex;align-items:center;justify-content:center;background:linear-gradient(180deg,#1e6fb0,var(--navy))}
  .tab span{transform:rotate(-90deg);color:#fff;font-weight:600;font-size:12px;letter-spacing:.6px;white-space:nowrap}
  .tab-1{left:58px}.tab-2{left:332px;background:var(--sky)}.tab-3{left:607px}

  .sec-title{font-weight:700;font-size:17.5px;color:var(--navy);letter-spacing:-.2px;white-space:nowrap}
  .sec-sub{font-weight:300;font-size:15px;color:#2e3340}

  .benefits-title{left:54px;top:614px}
  .benefits-sub{left:54px;top:637px}
  .col-divider{left:341px;top:617px;width:1px;height:326px;background:#e0e3e8}
  .timeline{left:74px;top:716px;height:228px;border-left:1.5px dotted var(--teal)}
  .benefit{left:54px;width:270px;display:flex;gap:13px}
  .benefit .shield{flex:none;width:41px;height:47px}
  .benefit h3{font-weight:600;font-size:14px;color:var(--teal);white-space:nowrap;line-height:18px}
  .benefit h3 i{font-style:normal;font-weight:300}
  .benefit p{font-weight:300;font-size:10px;line-height:12.6px;color:#3a3d46;margin-top:4px}
  .b1{top:672px}.b2{top:762px}.b3{top:854px}

  .work-title{left:369px;top:614px}
  .work-sub{left:369px;top:640px}
  .work-body{top:676px;font-weight:300;font-size:10px;line-height:12.6px;color:#3a3d46}
  .wb1{left:371px;width:216px}.wb2{left:605px;width:238px}

  .compare{top:760px;width:222px;height:110px;border-radius:22px;padding:14px 0 0 21px}
  .compare h4{display:flex;align-items:center;gap:6px;font-weight:500;font-size:16px;color:var(--navy);margin-bottom:8px}
  .compare li{list-style:none;display:flex;align-items:center;gap:5px;font-weight:400;font-size:10.5px;line-height:12.6px;color:#2b2e38}
  .term{left:371px;background:var(--mist)}
  .plan{left:603px;background:var(--ice);height:107px}
  .ic{flex:none;border-radius:50%;display:inline-flex;align-items:center;justify-content:center}

  .diff-title{left:369px;top:902px;width:487px;display:flex;align-items:center;gap:8px}
  .diff-title::after{content:"";flex:1;height:1px;background:var(--teal);margin-top:2px}
  .diff-sub{left:369px;top:924px}
  .feature{top:962px}
  .feature svg{height:40px;display:block}
  .feature h5{margin-top:18px;font-weight:600;font-size:15px;line-height:16px;color:var(--navy);letter-spacing:-.2px}
  .feature p{margin-top:7px;font-weight:300;font-size:10px;line-height:12px;color:#3a3d46}
  .f1{left:370px;width:96px}.f2{left:482px;width:96px}.f3{left:588px;width:100px}.f4{left:698px;width:88px}.f5{left:801px;width:82px}

  .cta{left:54px;top:966px;width:285px;height:194px;border-radius:26px 26px 0 0;background:linear-gradient(160deg,#1a5cb0 0%,#1f8fca 100%);padding:0 10px}
  .cta-top{display:flex;gap:16px;padding:16px 0 0 12px;height:94px}
  .cta-top svg{flex:none;width:62px;height:62px}
  .tagline{font-weight:600;font-size:19px;line-height:21px;color:#fff;white-space:nowrap}
  .tagline span{display:block}
  .tagline .accent{color:var(--sky)}
  .dash{border-top:1px dashed rgba(255,255,255,.55);margin:0 8px}
  .cta-line{display:flex;align-items:center;gap:9px;padding:7px 0 7px 18px}
  .env{flex:none;width:38px;height:38px;border-radius:50%;background:var(--sky);display:flex;align-items:center;justify-content:center}
  .cta-line p{font-weight:400;font-size:10.8px;line-height:12px;color:#fff}
  .credit{text-align:center;font-size:8.4px;color:#fff;padding-top:9px}
  .credit b{font-weight:700}

  .base-band{left:0;top:1146px;width:896px;height:14px;background:linear-gradient(90deg,var(--navy),#1a5cb0 55%,#1aa8d6)}
</style>
</head>
<body>
<main class="flyer">
  <div class="abs hero-photo" role="img" aria-label="Photo of a smiling family of three walking hand in hand along a sunny beach"></div>

  <div class="abs brand">
    <div class="brand-dot"></div>
    <div class="brand-name">Harbor Perks</div>
  </div>

  <div class="abs seal"><span class="top">GUARANTEED</span><span class="bottom">ISSUED</span></div>

  <h1 class="abs headline">One small decision.<br>A lifetime of protection.</h1>
  <p class="abs subhead">Permanent life insurance + long-term care<br>coverage, starting at <b>$1 a day.</b></p>

  <div class="abs rule-title choose"><span>CHOOSE YOUR DAILY INVESTMENT</span></div>

  <div class="abs tier tier-1">
    <div class="price"><strong>$1</strong><em>/ day</em></div>
    <svg class="arrow" viewBox="0 0 38 10"><path d="M1 5h34M31 1.5l4 3.5-4 3.5" stroke="#232b6b" stroke-width="1.3" fill="none"/></svg>
    <div class="amount">$20,000</div>
    <div class="label">Life Insurance</div>
  </div>
  <div class="abs tier tier-2">
    <div class="price"><strong>$2</strong><em>/ day</em></div>
    <svg class="arrow" viewBox="0 0 38 10"><path d="M1 5h34M31 1.5l4 3.5-4 3.5" stroke="#fff" stroke-width="1.3" fill="none"/></svg>
    <div class="amount">$40,000</div>
    <div class="label">Life Insurance</div>
    <div class="popular"><span><span style="color:var(--sky)">★</span> MOST POPULAR</span></div>
  </div>
  <div class="abs tier tier-3">
    <div class="price"><strong>$3</strong><em>/ day</em></div>
    <svg class="arrow" viewBox="0 0 38 10"><path d="M1 5h34M31 1.5l4 3.5-4 3.5" stroke="#232b6b" stroke-width="1.3" fill="none"/></svg>
    <div class="amount">$60,000</div>
    <div class="label">Life Insurance</div>
  </div>
  <div class="abs tab tab-1"><span>TIER 1</span></div>
  <div class="abs tab tab-2"><span>TIER 2</span></div>
  <div class="abs tab tab-3"><span>TIER 1</span></div>

  <div class="abs rule-title rate-note"><span><svg width="10" height="12" viewBox="0 0 10 12"><rect x="0.5" y="5" width="9" height="7" rx="1" fill="#232b6b"/><path d="M2.5 5V3.5a2.5 2.5 0 015 0V5" stroke="#232b6b" stroke-width="1.4" fill="none"/></svg>Rate locked at enrollment. Benefit never decreases.</span></div>

  <h2 class="abs sec-title benefits-title">THREE BENEFITS. ONE POLICY.</h2>
  <p class="abs sec-sub benefits-sub">Your money works three ways.</p>
  <div class="abs col-divider"></div>
  <div class="abs timeline"></div>

  <div class="abs benefit b1">
    <svg class="shield" viewBox="0 0 41 47"><path d="M20.5 1C27 4 33 5 40 5c0 20-6 33-19.5 41C7 38 1 25 1 5c7 0 13-1 19.5-4z" fill="#1a6fc0"/><g stroke="#fff" stroke-width="1.2" fill="none"><path d="M10 30h22M12 29v-4h3v4M17 29v-7h3v7M22 29v-9h3v9M27 29v-12h3v12M11 22l8-6 5 3 7-7M27 12h4v4"/></g></svg>
    <div><h3><i>01 |</i> Cash Value Growth</h3>
    <p>Averages 6% annually over the last 50 years — guaranteed never to fall below 3%. Better than any savings account. And if you ever need it, you can borrow against it. It's your money.</p></div>
  </div>
  <div class="abs benefit b2">
    <svg class="shield" viewBox="0 0 41 47"><path d="M20.5 1C27 4 33 5 40 5c0 20-6 33-19.5 41C7 38 1 25 1 5c7 0 13-1 19.5-4z" fill="#1a6fc0"/><g stroke="#fff" stroke-width="1.2" fill="none"><rect x="18" y="13" width="13" height="9" rx="1"/><circle cx="17" cy="21" r="5"/><path d="M8 28h6l5 2h6l3-3M8 33h5l6 2h6l6-5"/></g></svg>
    <div><h3><i>02 |</i> Tax-Free Death Benefit</h3>
    <p>From day one, your family is protected. The full benefit is paid tax-free to the person you choose — no waiting period, no exceptions. That's your legacy, preserved.</p></div>
  </div>
  <div class="abs benefit b3">
    <svg class="shield" viewBox="0 0 41 47"><path d="M20.5 1C27 4 33 5 40 5c0 20-6 33-19.5 41C7 38 1 25 1 5c7 0 13-1 19.5-4z" fill="#1a6fc0"/><g stroke="#fff" stroke-width="1.2" fill="none"><path d="M20.5 24c-5-3-7-6-5-8.5 1.7-2 4-1 5 .7 1-1.7 3.3-2.7 5-.7 2 2.5 0 5.5-5 8.5z"/><path d="M8 18l3 9 6 5v3M33 18l-3 9-6 5v3"/></g></svg>
    <div><h3><i>03 |</i> Long-Term Care Coverage</h3>
    <p>70% of Americans will need long-term care. This plan pays 75% of your benefit — upfront and tax-free — to cover those costs while you're still alive. Your retirement savings stay intact. Your family stays protected.</p></div>
  </div>

  <h2 class="abs sec-title work-title">ALREADY HAVE LIFE INSURANCE THROUGH WORK?</h2>
  <p class="abs sec-sub work-sub">That's term. It ends when you need it most.</p>
  <p class="abs work-body wb1">Term life insurance is designed for temporary needs — protecting your paycheck, your mortgage, your kids while they're home. When you retire, the house is paid off and your children are grown. Term ends because the need ends.</p>
  <p class="abs work-body wb2">But one need never ends: your final expenses and the cost of long-term care. This permanent plan stays with you after retirement — when term coverage is gone and getting new coverage is expensive or impossible.</p>

  <div class="abs compare term">
    <h4><span class="ic" style="width:14px;height:14px;background:var(--red)"><svg width="7" height="7" viewBox="0 0 7 7"><path d="M1 1l5 5M6 1L1 6" stroke="#fff" stroke-width="1.4"/></svg></span>TERM LIFE</h4>
    <ul>
      <li><span class="ic" style="width:8px;height:8px;background:var(--red)"><svg width="4" height="4" viewBox="0 0 4 4"><path d="M.5.5l3 3M3.5.5l-3 3" stroke="#fff" stroke-width=".9"/></svg></span>Gets more expensive with age</li>
      <li><span class="ic" style="width:8px;height:8px;background:var(--red)"><svg width="4" height="4" viewBox="0 0 4 4"><path d="M.5.5l3 3M3.5.5l-3 3" stroke="#fff" stroke-width=".9"/></svg></span>Ends at retirement</li>
      <li><span class="ic" style="width:8px;height:8px;background:var(--red)"><svg width="4" height="4" viewBox="0 0 4 4"><path d="M.5.5l3 3M3.5.5l-3 3" stroke="#fff" stroke-width=".9"/></svg></span>No cash value</li>
      <li><span class="ic" style="width:8px;height:8px;background:var(--red)"><svg width="4" height="4" viewBox="0 0 4 4"><path d="M.5.5l3 3M3.5.5l-3 3" stroke="#fff" stroke-width=".9"/></svg></span>Temporary protection only</li>
    </ul>
  </div>
  <div class="abs compare plan">
    <h4><span class="ic" style="width:14px;height:14px;background:var(--green)"><svg width="8" height="7" viewBox="0 0 8 7"><path d="M1 3.5l2 2L7 1" stroke="#fff" stroke-width="1.4" fill="none"/></svg></span>THIS PLAN</h4>
    <ul>
      <li><span class="ic" style="width:8px;height:8px;background:var(--green)"><svg width="5" height="4" viewBox="0 0 5 4"><path d="M.5 2l1.3 1.3L4.5.5" stroke="#fff" stroke-width=".9" fill="none"/></svg></span>Rate locked forever at enrollment</li>
      <li><span class="ic" style="width:8px;height:8px;background:var(--green)"><svg width="5" height="4" viewBox="0 0 5 4"><path d="M.5 2l1.3 1.3L4.5.5" stroke="#fff" stroke-width=".9" fill="none"/></svg></span>Stays with you after retirement</li>
      <li><span class="ic" style="width:8px;height:8px;background:var(--green)"><svg width="5" height="4" viewBox="0 0 5 4"><path d="M.5 2l1.3 1.3L4.5.5" stroke="#fff" stroke-width=".9" fill="none"/></svg></span>Builds real cash value</li>
      <li><span class="ic" style="width:8px;height:8px;background:var(--green)"><svg width="5" height="4" viewBox="0 0 5 4"><path d="M.5 2l1.3 1.3L4.5.5" stroke="#fff" stroke-width=".9" fill="none"/></svg></span>Permanent protection for life</li>
    </ul>
  </div>

  <h2 class="abs sec-title diff-title">WHAT MAKES THIS DIFFERENT</h2>
  <p class="abs sec-sub diff-sub">Built for you. Stays with you.</p>

  <div class="abs feature f1">
    <svg viewBox="0 0 36 40" width="36"><g fill="none" stroke="#1a6fc0" stroke-width="1.6"><rect x="3" y="3" width="30" height="28" rx="2"/><path d="M1 35h34"/><path d="M18 8c3 1.5 5 2 8 2 0 8-3 12-8 15-5-3-8-7-8-15 3 0 5-.5 8-2z"/><path d="M14.5 16.5l2.5 2.5 4.5-5"/></g></svg>
    <h5>Guaranteed Issued</h5>
    <p>No medical exams. No questions asked. You qualify.</p>
  </div>
  <div class="abs feature f2">
    <svg viewBox="0 0 38 40" width="38"><g fill="none" stroke="#1a6fc0" stroke-width="1.4"><circle cx="11" cy="8" r="3.5"/><circle cx="19" cy="6" r="3.5"/><circle cx="27" cy="8" r="3.5"/><path d="M5 22v-5a6 6 0 0112 0M13 17a6 6 0 0112 0M21 17a6 6 0 0112 0v5"/><circle cx="15" cy="22" r="3"/><circle cx="23" cy="22" r="3"/><path d="M9 33a6 6 0 0112 0M17 33a6 6 0 0112 0"/></g></svg>
    <h5>Group<br>Rate</h5>
    <p>Because you work here, you get pricing individuals can't access on their own.</p>
  </div>
  <div class="abs feature f3">
    <svg viewBox="0 0 30 40" width="28"><g fill="none" stroke="#1a6fc0" stroke-width="1.8"><path d="M7 17V10a8 8 0 0116 0v7"/><rect x="2" y="17" width="26" height="21" rx="2"/><circle cx="15" cy="26" r="3"/><path d="M15 29v4"/></g></svg>
    <h5>Rate Locked<br>Forever</h5>
    <p>Your premium never increases. Your benefit never decreases.</p>
  </div>
  <div class="abs feature f4">
    <svg viewBox="0 0 44 40" width="44"><g fill="none" stroke="#1a6fc0" stroke-width="1.5"><path d="M14 10V6h12v4"/><rect x="2" y="10" width="36" height="24" rx="2"/><path d="M2 20h36"/><rect x="8" y="17" width="4" height="6"/><circle cx="32" cy="24" r="7"/><path d="M27 29l-7 7"/></g></svg>
    <h5>Portable</h5>
    <p>Change jobs. Retire. Your policy comes with you at the same rate.</p>
  </div>
  <div class="abs feature f5">
    <svg viewBox="0 0 34 40" width="32"><g fill="none" stroke="#1a6fc0" stroke-width="1.4"><circle cx="9" cy="9" r="3"/><circle cx="21" cy="9" r="3"/><path d="M4 22v-4a5 5 0 0110 0v4M16 22v-4a5 5 0 0110 0v4"/><circle cx="15" cy="21" r="2.3"/><path d="M11 29a4 4 0 018 0"/><path d="M27 3v6M24 6h6"/><path d="M2 33c6 0 8 3 14 3h8l8-6"/></g></svg>
    <h5>Family<br>Coverage</h5>
    <p>Protect your spouse and children under the same plan.</p>
  </div>

  <section class="abs cta">
    <div class="cta-top">
      <svg viewBox="0 0 62 62"><g fill="none" stroke="#fff" stroke-width="1.6"><path d="M34 4c6 3 12 4 20 4 0 18-6 30-20 38-14-8-20-20-20-38 8 0 14-1 20-4z"/><path d="M24 24a10 10 0 0120 0zM34 24v10a3 3 0 01-5 1"/><path d="M2 42h8l8-4h10a3 3 0 010 6h-8M2 54h10l10 3 18-11a3 3 0 00-4-5l-10 6"/></g></svg>
      <p class="tagline"><span>Protect retirement.</span><span class="accent">Preserve dignity.</span><span>Plan ahead.</span></p>
    </div>
    <div class="dash"></div>
    <div class="cta-line">
      <div class="env"><svg width="22" height="15" viewBox="0 0 22 15"><rect x="1" y="1" width="20" height="13" fill="none" stroke="#fff" stroke-width="1.3"/><path d="M1 1l10 8 10-8M1 14l7-6M21 14l-7-6" fill="none" stroke="#fff" stroke-width="1.1"/></svg></div>
      <p>Be on the lookout for your personalized<br>coverage details.</p>
    </div>
    <div class="dash"></div>
    <p class="credit">Brokered by Harbor Perks · Underwritten by <b>TrueLedger</b></p>
  </section>

  <div class="abs base-band"></div>
</main>
</body>
</html>
```